Medical Practice Business Card

we need a business card for our new medical ophthalmology practice based in Needham Massachusetts. we are looking for a simple , modern and elegant design.
the card needs to contain the following
1- the logo of our practice (please see attached file)
2- the name of the practice : "Silver Birch Retina Care"
3- Doctor's Name: Tobias Rendell MD PhD
4- Specialty: Board-Certified Vitreoretinal Surgeon
5- practice address: 87 Larkspur Ave, Suite 210, Needham MA 02481
7- Office number: 617- 482 - 7730
8- fax number: 617- 391 - 2268
9- email: info@sbretinahub.example
10- website: www.sbretinahub.example

```html
<!DOCTYPE html>
<html lang="en">
<head>
<meta charset="utf-8">
<title>Silver Birch Retina Care – Business Card</title>
<link rel="stylesheet" href="https://fonts.googleapis.com/css2?family=Cinzel:wght@700&family=Poppins:wght@400&family=Roboto:ital,wght@0,400;1,400&display=swap">
<style>
  :root {
    --page-bg: #6c6c6c;
    --card-bg: #ffffff;
    --navy: #1b3966;
    --royal: #0b4d97;
    --royal-deep: #0a3d7a;
    --cyan: #7ed4e8;
    --ink: #1e1e1e;
    --label-grey: #8a8a8a;
    --rule-grey: #d6d6d6;
  }
  * { margin: 0; padding: 0; box-sizing: border-box; }
  html, body { width: 1093px; height: 1200px; overflow: hidden; }
  body { background: var(--page-bg); position: relative; font-family: "Poppins", sans-serif; }

  .card {
    position: absolute;
    background: var(--card-bg);
    border-radius: 24px;
    overflow: hidden;
    box-shadow: 3px 4px 3px rgba(0,0,0,0.55);
  }
  .card--front { left: 265px; top: 226px; width: 577px; height: 356px; }
  .card--back  { left: 265px; top: 621px; width: 581px; height: 356px; }

  /* Front */
  .brand {
    position: absolute; right: 24px; top: 46px;
    display: flex; align-items: center; gap: 14px;
  }
  .brand__mark { width: 12px; height: 12px; border-radius: 50%; background: var(--navy); flex: none; }
  .brand__name {
    font-family: "Poppins", sans-serif; font-weight: 400; color: var(--navy);
    font-size: 25px; line-height: 32px; text-align: left;
  }
  .doctor { position: absolute; left: 31px; top: 180px; }
  .doctor__name {
    font-family: "Cinzel", serif; font-weight: 700; color: var(--navy);
    font-size: 29px; line-height: 34px;
  }
  .doctor__title { font-size: 17.5px; line-height: 22px; color: var(--ink); }
  .divider { position: absolute; left: 31px; top: 241px; width: 518px; height: 1px; background: #555; }

  .contact { position: absolute; top: 252px; font-size: 18px; line-height: 21px; color: var(--ink); }
  .contact--phones { left: 31px; }
  .contact--web { right: 25px; text-align: right; }
  .contact__row { display: flex; align-items: center; gap: 7px; }
  .contact--web .contact__row { justify-content: flex-end; }
  .contact__icon { width: 16px; height: 16px; fill: var(--navy); flex: none; }
  .contact__icon--outline { fill: none; stroke: var(--navy); stroke-width: 2; }
  .accent { color: var(--royal); }

  .swoosh { position: absolute; left: 0; top: 296px; }
  .footer-band {
    position: absolute; left: 0; bottom: 0; width: 100%; height: 45px;
    background: linear-gradient(180deg, var(--royal), var(--royal-deep));
    color: #fff; font-size: 17.5px; line-height: 45px; text-align: center;
  }

  /* Back */
  .appt__title {
    position: absolute; top: 36px; left: 0; width: 100%; padding-left: 36px;
    text-align: center; font-family: "Cinzel", serif; font-weight: 700;
    font-size: 26px; color: var(--navy);
  }
  .field {
    position: absolute; left: 79px; width: 421px;
    border-bottom: 1px solid var(--rule-grey);
    font-family: "Roboto", sans-serif; font-size: 22px; color: var(--label-grey);
    display: flex; justify-content: space-between; line-height: 24px;
  }
  .field--name { top: 98px; }
  .field--when { top: 152px; }
  .field--note { top: 216px; }
  .field--blank { top: 284px; height: 1px; }
  .field__time { margin-left: 92px; }
  .appt__notice {
    position: absolute; top: 301px; left: 0; width: 100%; padding-left: 12px;
    text-align: center; font-family: "Roboto", sans-serif; font-style: italic;
    font-size: 15px; color: #333;
  }
</style>
</head>
<body>

<section class="card card--front">
  <div class="brand">
    <span class="brand__mark"></span>
    <div class="brand__name">Silver Birch<br>Retina Care</div>
  </div>

  <div class="doctor">
    <h1 class="doctor__name">Tobias Rendell MD PhD</h1>
    <p class="doctor__title">Board-Certified Vitreoretinal Surgeon</p>
  </div>
  <div class="divider"></div>

  <div class="contact contact--phones">
    <div class="contact__row">
      <svg class="contact__icon" viewBox="0 0 24 24"><path d="M6.6 10.8a15.1 15.1 0 0 0 6.6 6.6l2.2-2.2a1 1 0 0 1 1-.25 11.4 11.4 0 0 0 3.6.57 1 1 0 0 1 1 1V20a1 1 0 0 1-1 1A17 17 0 0 1 3 4a1 1 0 0 1 1-1h3.5a1 1 0 0 1 1 1c0 1.25.2 2.45.57 3.6a1 1 0 0 1-.25 1z"/></svg>
      <span>617 - 482 - 7730</span>
    </div>
    <div class="contact__row">
      <svg class="contact__icon" viewBox="0 0 24 24"><path d="M7 2h10v5H7zM4 8h16a2 2 0 0 1 2 2v7h-4v5H6v-5H2v-7a2 2 0 0 1 2-2zm4 8v4h8v-4z"/></svg>
      <span>617 - 391 - 2268</span>
    </div>
  </div>

  <div class="contact contact--web">
    <div class="contact__row">
      <span>info@sbretinahub.example</span>
      <svg class="contact__icon" viewBox="0 0 24 24"><path d="M2 5h20v14H2zm2 2v.5l8 5.5 8-5.5V7z"/></svg>
    </div>
    <div class="contact__row">
      <span>www.<span class="accent">sbretinahub</span>.example</span>
      <svg class="contact__icon contact__icon--outline" viewBox="0 0 24 24"><circle cx="12" cy="12" r="9"/><path d="M3 12h18M12 3c3 3 3 15 0 18M12 3c-3 3-3 15 0 18"/></svg>
    </div>
  </div>

  <svg class="swoosh" width="577" height="22" viewBox="0 0 577 22">
    <path d="M11 11 L480 10" stroke="#7ed4e8" stroke-width="2"/>
    <path d="M20 14 Q300 7 577 14 L577 16 L20 16 Z" fill="#0b4d97"/>
    <circle cx="11" cy="11" r="10" fill="#7ed4e8" stroke="#fff" stroke-width="2"/>
  </svg>

  <div class="footer-band">87 Larkspur Ave, Suite 210, Needham MA 02481</div>
</section>

<section class="card card--back">
  <h2 class="appt__title">NEXT APPOINTMENT</h2>
  <div class="field field--name"><span>NAME</span></div>
  <div class="field field--when"><span>DATE</span><span class="field__time">TIME</span><span>AM/PM</span></div>
  <div class="field field--note"><span>Note</span></div>
  <div class="field field--blank"></div>
  <p class="appt__notice">If unable to keep appointment, kindly give 24hrs notice.</p>
</section>

</body>
</html>
```